LEARN Business Skills so you can Earn a good living

size of the poster is 8”x 10.75" plus 0.25" bleed.
Please leave 1 inch on the bottoum for footer
I want a design a poster that will attract people's attention.
I appreciate a creative ad however the ad should not take away from being able to clearly read the text.
-I also appreciate a simple creative ad that is not too busy.
-you can use graphics, vectors, or pictures of real people.
-however, if you use real people it should be a white male that is wearing a white shirt and look like a professional person.

Target Market(s)

Potential young business people

Industry/Entity Type

education

Requirements
Must have
• easy to read the text
Nice to have
• I would like a "creative" simple ad that is easy to be read
Should not have
• pictures of women

```html
<!DOCTYPE html>
<html lang="en">
<head>
<meta charset="utf-8">
<title>Learn to Earn – Business Enrichment Course</title>
<link href="https://fonts.googleapis.com/css2?family=Oswald:wght@600;700&family=Montserrat:ital,wght@0,400;0,500;0,700;1,800&display=swap" rel="stylesheet">
<style>
  :root {
    --cyan: #13b4dc;
    --cyan-light: #22d6f0;
    --cyan-deep: #0a8fbd;
    --navy: #0c3a63;
    --ink: #2b2f36;
    --muted: #5a6068;
    --paper: #ffffff;
    --paper-shade: #e6e8ec;
    --divider: #c9ccd2;
  }
  * { margin: 0; padding: 0; box-sizing: border-box; }
  html, body { width: 1045px; height: 1200px; overflow: hidden; background: #f2f3f5; }
  .poster {
    position: relative;
    width: 1045px; height: 1200px; overflow: hidden;
    background: radial-gradient(ellipse at 70% 35%, var(--paper) 0%, #f3f4f6 45%, var(--paper-shade) 100%);
    font-family: "Montserrat", sans-serif;
    color: var(--ink);
  }
  .headline {
    position: absolute; left: 60px; top: 40px;
    font-family: "Oswald", sans-serif; font-weight: 700;
    font-size: 150px; line-height: 1; letter-spacing: 1px;
    color: var(--cyan);
    text-transform: uppercase;
  }
  .headline .small { text-transform: none; font-size: 0.9em; }
  .course-pill {
    position: absolute; left: 70px; top: 210px;
    background: var(--navy); color: var(--paper);
    border-radius: 40px; padding: 8px 34px;
    font-weight: 800; font-style: italic; font-size: 36px;
  }
  .intro {
    position: absolute; left: 80px; top: 290px;
    font-size: 22px; font-weight: 700; line-height: 1.3; color: var(--ink);
  }
  .benefits {
    position: absolute; left: 70px; top: 370px;
    display: flex; width: 520px;
  }
  .benefit {
    flex: 1; text-align: center; padding-top: 10px;
    border-left: 1px solid var(--divider);
  }
  .benefit:first-child { border-left: none; }
  .benefit svg { width: 92px; height: 92px; display: block; margin: 0 auto 10px; }
  .benefit p { font-size: 16px; color: var(--muted); line-height: 1.3; }
  .subject-list {
    position: absolute; left: 80px; top: 540px;
    list-style: none; font-size: 18px; line-height: 23px; color: var(--ink);
  }
  .subject-list li { display: flex; align-items: center; gap: 10px; }
  .subject-list svg { width: 14px; height: 14px; flex: none; }
  .portrait {
    position: absolute; left: 560px; top: 330px; width: 440px; height: 710px;
    background: linear-gradient(180deg, #d9dde3 0%, #eef1f5 40%, #cfd6df 100%);
    border-radius: 200px 200px 0 0;
  }
  .accent-band {
    position: absolute; left: 0; top: 1040px; width: 1045px; height: 40px;
    background: linear-gradient(90deg, var(--cyan-deep), var(--cyan-light));
  }
  .footer {
    position: absolute; left: 0; bottom: 0; width: 1045px; height: 112px;
    background: linear-gradient(180deg, var(--cyan-light), var(--cyan-deep));
  }
</style>
</head>
<body>
<main class="poster">
  <h1 class="headline">Learn <span class="small">to</span> Earn</h1>
  <div class="course-pill">Business Enrichment Course</div>
  <p class="intro">A proven success of helping people in their livelihoods<br>Business skills that will help you:</p>

  <section class="benefits">
    <div class="benefit">
      <svg viewBox="0 0 92 92" aria-hidden="true">
        <circle cx="46" cy="46" r="44" fill="var(--cyan)" stroke="var(--paper)" stroke-width="3"/>
        <rect x="30" y="26" width="32" height="40" rx="3" fill="var(--navy)"/>
        <path d="M37 40h18M37 48h18M37 56h12" stroke="var(--paper)" stroke-width="3"/>
      </svg>
      <p>Get a<br>quality job</p>
    </div>
    <div class="benefit">
      <svg viewBox="0 0 92 92" aria-hidden="true">
        <circle cx="46" cy="46" r="44" fill="var(--cyan)" stroke="var(--paper)" stroke-width="3"/>
        <path d="M26 66h42" stroke="var(--navy)" stroke-width="3"/>
        <rect x="30" y="52" width="7" height="14" fill="var(--navy)"/>
        <rect x="41" y="44" width="7" height="22" fill="var(--navy)"/>
        <rect x="52" y="36" width="7" height="30" fill="var(--navy)"/>
        <path d="M28 46l14-12 8 6 16-14" fill="none" stroke="var(--paper)" stroke-width="3"/>
        <path d="M60 24h7v7" fill="none" stroke="var(--paper)" stroke-width="3"/>
      </svg>
      <p>start/grow<br>your business</p>
    </div>
    <div class="benefit">
      <svg viewBox="0 0 92 92" aria-hidden="true">
        <circle cx="46" cy="46" r="44" fill="var(--cyan)" stroke="var(--paper)" stroke-width="3"/>
        <text x="46" y="60" text-anchor="middle" font-family="Montserrat, sans-serif" font-weight="700" font-size="40" fill="var(--navy)">$</text>
        <path d="M26 68l12-12M60 32l8-8M62 24h6v6" fill="none" stroke="var(--paper)" stroke-width="3"/>
      </svg>
      <p>Increase<br>your salary</p>
    </div>
  </section>

  <ul class="subject-list">
    <li><svg viewBox="0 0 15 15" aria-hidden="true"><rect x="1" y="1" width="13" height="13" fill="none" stroke="var(--ink)" stroke-width="1.5"/><path d="M3.5 7.5l3 3 5-6" fill="none" stroke="var(--ink)" stroke-width="1.8"/></svg>Business Administration</li>
    <li><svg viewBox="0 0 15 15" aria-hidden="true"><rect x="1" y="1" width="13" height="13" fill="none" stroke="var(--ink)" stroke-width="1.5"/><path d="M3.5 7.5l3 3 5-6" fill="none" stroke="var(--ink)" stroke-width="1.8"/></svg>Small Business Management</li>
    <li><svg viewBox="0 0 15 15" aria-hidden="true"><rect x="1" y="1" width="13" height="13" fill="none" stroke="var(--ink)" stroke-width="1.5"/><path d="M3.5 7.5l3 3 5-6" fill="none" stroke="var(--ink)" stroke-width="1.8"/></svg>Finance</li>
    <li><svg viewBox="0 0 15 15" aria-hidden="true"><rect x="1" y="1" width="13" height="13" fill="none" stroke="var(--ink)" stroke-width="1.5"/><path d="M3.5 7.5l3 3 5-6" fill="none" stroke="var(--ink)" stroke-width="1.8"/></svg>Investments</li>
    <li><svg viewBox="0 0 15 15" aria-hidden="true"><rect x="1" y="1" width="13" height="13" fill="none" stroke="var(--ink)" stroke-width="1.5"/><path d="M3.5 7.5l3 3 5-6" fill="none" stroke="var(--ink)" stroke-width="1.8"/></svg>Computers</li>
    <li><svg viewBox="0 0 15 15" aria-hidden="true"><rect x="1" y="1" width="13" height="13" fill="none" stroke="var(--ink)" stroke-width="1.5"/><path d="M3.5 7.5l3 3 5-6" fill="none" stroke="var(--ink)" stroke-width="1.8"/></svg>Accounting</li>
    <li><svg viewBox="0 0 15 15" aria-hidden="true"><rect x="1" y="1" width="13" height="13" fill="none" stroke="var(--ink)" stroke-width="1.5"/><path d="M3.5 7.5l3 3 5-6" fill="none" stroke="var(--ink)" stroke-width="1.8"/></svg>Sales Marketing</li>
    <li><svg viewBox="0 0 15 15" aria-hidden="true"><rect x="1" y="1" width="13" height="13" fill="none" stroke="var(--ink)" stroke-width="1.5"/><path d="M3.5 7.5l3 3 5-6" fill="none" stroke="var(--ink)" stroke-width="1.8"/></svg>Project Management</li>
    <li><svg viewBox="0 0 15 15" aria-hidden="true"><rect x="1" y="1" width="13" height="13" fill="none" stroke="var(--ink)" stroke-width="1.5"/><path d="M3.5 7.5l3 3 5-6" fill="none" stroke="var(--ink)" stroke-width="1.8"/></svg>Interviewing Skills</li>
    <li><svg viewBox="0 0 15 15" aria-hidden="true"><rect x="1" y="1" width="13" height="13" fill="none" stroke="var(--ink)" stroke-width="1.5"/><path d="M3.5 7.5l3 3 5-6" fill="none" stroke="var(--ink)" stroke-width="1.8"/></svg>Business Law</li>
    <li><svg viewBox="0 0 15 15" aria-hidden="true"><rect x="1" y="1" width="13" height="13" fill="none" stroke="var(--ink)" stroke-width="1.5"/><path d="M3.5 7.5l3 3 5-6" fill="none" stroke="var(--ink)" stroke-width="1.8"/></svg>Negotiation</li>
    <li><svg viewBox="0 0 15 15" aria-hidden="true"><rect x="1" y="1" width="13" height="13" fill="none" stroke="var(--ink)" stroke-width="1.5"/><path d="M3.5 7.5l3 3 5-6" fill="none" stroke="var(--ink)" stroke-width="1.8"/></svg>Public Speaking</li>
    <li><svg viewBox="0 0 15 15" aria-hidden="true"><rect x="1" y="1" width="13" height="13" fill="none" stroke="var(--ink)" stroke-width="1.5"/><path d="M3.5 7.5l3 3 5-6" fill="none" stroke="var(--ink)" stroke-width="1.8"/></svg>Import/export</li>
    <li><svg viewBox="0 0 15 15" aria-hidden="true"><rect x="1" y="1" width="13" height="13" fill="none" stroke="var(--ink)" stroke-width="1.5"/><path d="M3.5 7.5l3 3 5-6" fill="none" stroke="var(--ink)" stroke-width="1.8"/></svg>Information Technology</li>
    <li><svg viewBox="0 0 15 15" aria-hidden="true"><rect x="1" y="1" width="13" height="13" fill="none" stroke="var(--ink)" stroke-width="1.5"/><path d="M3.5 7.5l3 3 5-6" fill="none" stroke="var(--ink)" stroke-width="1.8"/></svg>Distribution</li>
    <li><svg viewBox="0 0 15 15" aria-hidden="true"><rect x="1" y="1" width="13" height="13" fill="none" stroke="var(--ink)" stroke-width="1.5"/><path d="M3.5 7.5l3 3 5-6" fill="none" stroke="var(--ink)" stroke-width="1.8"/></svg>Marketing</li>
    <li><svg viewBox="0 0 15 15" aria-hidden="true"><rect x="1" y="1" width="13" height="13" fill="none" stroke="var(--ink)" stroke-width="1.5"/><path d="M3.5 7.5l3 3 5-6" fill="none" stroke="var(--ink)" stroke-width="1.8"/></svg>Ledgerwise</li>
    <li><svg viewBox="0 0 15 15" aria-hidden="true"><rect x="1" y="1" width="13" height="13" fill="none" stroke="var(--ink)" stroke-width="1.5"/><path d="M3.5 7.5l3 3 5-6" fill="none" stroke="var(--ink)" stroke-width="1.8"/></svg>Real Estate</li>
    <li><svg viewBox="0 0 15 15" aria-hidden="true"><rect x="1" y="1" width="13" height="13" fill="none" stroke="var(--ink)" stroke-width="1.5"/><path d="M3.5 7.5l3 3 5-6" fill="none" stroke="var(--ink)" stroke-width="1.8"/></svg>Health Care Management</li>
    <li><svg viewBox="0 0 15 15" aria-hidden="true"><rect x="1" y="1" width="13" height="13" fill="none" stroke="var(--ink)" stroke-width="1.5"/><path d="M3.5 7.5l3 3 5-6" fill="none" stroke="var(--ink)" stroke-width="1.8"/></svg>Shopstream</li>
  </ul>

  <div class="portrait" role="img" aria-label="Photo of a smiling professional man in a white shirt and navy tie, arms crossed"></div>

  <div class="accent-band"></div>
  <footer class="footer"></footer>
</main>
</body>
</html>
```